Talent Agency Needs Identity!

We are Copper Harbor Artists Inc. - a full service entertainment services agency that focuses primarily on securing contracts for musicians and entertainers aboard luxury cruise ships, however we are not limited exclusively to that area, as we are expanding into the areas of film and television.

We are looking for the perfect website and logo from the right designer!

We already own the domain www.copperharborartists-demo.com

The homepage only needs to be designed for this contest, unless you really want to go that extra mile!

Would like full HTML and CSS3 if applicable.

Logo needs to be designed as well.

We have two primary colors that we want to use - Lime green and grey (or charcoal, slate, graphite etc.)

The pages should be mostly slate colored background, slightly peppered with green accents, tastefully incorporated.

The key target audience of the website will be artists and musicians seeking representation, but also entertainment executives sourcing our talent. We are focused on a refined, legitimate, clever image.

Some ideas for pages we have:
Home Page
About Us
Life At Sea
Apply Now
Contact Us
FAQ
Members Only Section

Some ideas for inspiration can be found at:
www.varnowtalent-demo.com
www.perkisound-demo.com
www.tidewrenhub-demo.com
www.quilbar-demo.com
www.delvoria-demo.com

The logo needs to be designed as well.

The logo should be simple, and communicate creativity, legitimacy, and current trends. Just a simple word logo. "Copper Harbor Artists", again with a refined, professional look and feel, with elements of creativity and cleverness incorporated.

We plan to expand into the areas of film and television - so this can be considered in the final design, which is why we have chosen the name Copper Harbor to begin with.

The term Copper Harbor in the context of the film industry means to formally approve a project's production finance, thereby allowing the project to move forward from the development phase to pre-production and principal photography.

Therefore, we want our image to be 'forward thinking and feeling'.

The website should be SEO optimized and include the following keywords:

cruise ship music gigs musicians jobs

Target Market(s)

Musicians, entertainment executives/buyers

Industry/Entity Type

Entertainment

Requirements
Must have
• Simple, easy to navigate design. An example of a website far too complicated:
www.rakuvance-demo.com

An example of a nice, clean website we like:
www.varnowtalent-demo.com
www.delvoria-demo.com
www.quilbar-demo.com
Nice to have
• A members only section where talent can log in to see their recruitment info.

A page for talent buyers.

A clean, enticing home page, leaving you curious to explore.

Should not have
• A busy, difficult to navigate interface.

Cheesy looking clip art.

```html
<!DOCTYPE html>
<html lang="en">
<head>
<meta charset="utf-8">
<title>Copper Harbor Artists – Cruise Ship Music Gigs &amp; Musicians Jobs</title>
<link href="https://fonts.googleapis.com/css2?family=Bebas+Neue&family=Oswald:wght@300;400;500&family=PT+Sans:wght@400;700&display=swap" rel="stylesheet">
<style>
:root{
  --lime:#a9cc3c;
  --lime-bright:#b8d84a;
  --lime-dark:#8fb02a;
  --charcoal:#2d2d2d;
  --charcoal-deep:#1f1f1f;
  --card:#222222;
  --ink:#3a3a3a;
  --muted:#8a8a8a;
  --body:#a9a9a9;
  --white:#ffffff;
}
*{margin:0;padding:0;box-sizing:border-box}
html,body{width:1200px;height:1114px;overflow:hidden}
body{position:relative;background:var(--charcoal);font-family:"PT Sans",sans-serif;color:var(--body)}

.hero{position:absolute;left:0;top:0;width:1200px;height:450px;
  background:radial-gradient(ellipse at 50% 40%,#f4f4f4 0%,#d9d9d9 55%,#bdbdbd 100%)}
.hero-portrait{position:absolute;left:206px;top:69px;width:291px;height:381px;
  background:radial-gradient(ellipse at 50% 40%,#6a4a3a 0%,#4a3026 45%,rgba(80,60,50,0) 75%)}
.accent-band{position:absolute;left:0;top:450px;width:1200px;height:11px;background:var(--lime)}

.site-header{position:absolute;left:171px;top:0;width:858px;height:63px;background:var(--white);box-shadow:0 1px 4px rgba(0,0,0,.15)}
.brand{position:absolute;left:20px;top:14px;display:flex;align-items:center;gap:8px;
  font-family:"Oswald",sans-serif;font-weight:400;font-size:27px;color:var(--lime-dark);letter-spacing:-.3px}
.brand-dot{width:18px;height:18px;border-radius:50%;background:var(--lime)}
.main-nav{position:absolute;right:21px;top:23px;display:flex;gap:22px}
.main-nav a{font-family:"Oswald",sans-serif;font-weight:300;font-size:13.5px;color:var(--ink);text-decoration:none}

.hero-panel{position:absolute;left:573px;top:104px;width:429px;height:310px;
  background:linear-gradient(180deg,rgba(120,120,120,.55),rgba(110,110,110,.6))}
.hero-title{position:absolute;left:12px;top:7px;font-family:"Bebas Neue",sans-serif;font-weight:400;
  font-size:48px;line-height:50px;color:var(--white);letter-spacing:.8px;white-space:nowrap}
.hero-title span.line{display:block}
.hero-title .dark{color:#333}
.hero-title .lime{color:var(--lime-bright)}
.hero-rule{position:absolute;left:14px;right:14px;top:164px;height:1px;background:rgba(255,255,255,.45)}
.hero-copy{position:absolute;left:16px;top:173px;width:400px;font-size:12px;line-height:20.5px;color:#242424}
.apply-btn{position:absolute;left:128px;top:249px;width:166px;height:43px;border:2px solid #d3ea7d;
  background:linear-gradient(180deg,#c2e05a,#96bb2a);color:var(--white);font-family:"Oswald",sans-serif;font-weight:500;
  font-size:18px;letter-spacing:2px;display:flex;align-items:center;justify-content:center;text-decoration:none}

.section-title{position:absolute;left:0;width:1200px;top:481px;text-align:center;font-family:"Oswald",sans-serif;
  font-weight:300;font-size:21px;color:var(--white);letter-spacing:.6px}
.section-title .lime{color:var(--lime)}
.section-title svg{vertical-align:-1px;margin-right:5px}
.dots{position:absolute;left:171px;width:858px;height:2px;
  background:radial-gradient(circle,#5b5b5b 1px,transparent 1.2px) 0 0/8.6px 2px repeat-x}

.categories{position:absolute;left:171px;top:549px;display:flex;gap:11px}
.category{width:206px;height:169px;background:var(--card);text-align:center}
.category-photo{height:86px}
.category h3{margin-top:8px;font-family:"Oswald",sans-serif;font-weight:300;font-size:13.5px;color:var(--lime)}
.category p{margin:6px 14px 0;font-size:10px;line-height:15.5px;color:#6c6c6c}

.feature{position:absolute;left:173px;top:780px;width:856px}
.feature-photo{float:left;width:238px;height:101px;background:#1a1a1a;padding:8px;margin:0 20px 6px 0}
.feature-photo div{width:100%;height:100%;background:linear-gradient(180deg,#2a55b0,#1c3c86 70%,#2a3a6a)}
.feature h2{font-family:"Oswald",sans-serif;font-weight:300;font-size:13.5px;color:var(--lime);margin:0 0 6px 0}
.feature p{font-size:12.6px;line-height:20.5px;color:var(--body);padding-left:3px}
.feature a{color:var(--lime);text-decoration:none}
.read-more{margin-left:10px}

.site-footer{position:absolute;left:0;top:1014px;width:1200px;height:100px;background:var(--charcoal-deep)}
.copyright{position:absolute;left:172px;top:45px;font-size:11px;letter-spacing:.5px;color:#aaa}
.copyright a{color:var(--lime);text-decoration:none}
.footer-nav{position:absolute;right:173px;top:45px;display:flex;gap:21px}
.footer-nav a{font-size:11px;letter-spacing:.5px;color:#aaa;text-decoration:none}
.footer-nav a.current{color:var(--lime)}
</style>
</head>
<body>

<section class="hero" role="img" aria-label="Soft-focus piano keys backdrop">
  <div class="hero-portrait" role="img" aria-label="Portrait of a featured performer"></div>
</section>
<div class="accent-band"></div>

<header class="site-header">
  <div class="brand"><span class="brand-dot"></span>COPPER HARBOR ARTISTS</div>
  <nav class="main-nav">
    <a href="#">ABOUT US</a><a href="#">JOBS &amp; AUDITIONS</a><a href="#">EMPLOYERS</a><a href="#">FAQ</a><a href="#">CONTACT US</a>
  </nav>
</header>

<div class="hero-panel">
  <h1 class="hero-title"><span class="line">WE ARE A <span class="dark">FULL SERVICE</span></span><span class="line">ENTERTAINMENT AGENCY</span><span class="line">FOR <span class="lime">ARTISTS &amp; MUSICIANS</span></span></h1>
  <div class="hero-rule"></div>
  <p class="hero-copy">Lorem ipsum dolor sit amet, consectetur adipiscing elit. Aenean ac massa eu nunc ultricies interdum nec at eros. In et tempor odioters erents. Quisque in orci turpis. Integer posuere rhoncus semper sed tincidunt uto</p>
  <a class="apply-btn" href="#">APPLY NOW</a>
</div>

<h2 class="section-title"><svg width="16" height="16" viewBox="0 0 16 16"><path d="M8 1l1.8 4.6L14.5 6l-3.7 3 1.2 4.8L8 11.2 4 13.8l1.2-4.8L1.5 6l4.7-.4z" fill="#a9cc3c"/></svg>MAECENAS VESTIBULUM MAGNA UT LACUS DAPIBUS <span class="lime">SED MOLLIS QUAM DAPIBUS.</span></h2>
<div class="dots" style="top:525px"></div>

<div class="categories">
  <article class="category">
    <div class="category-photo" role="img" aria-label="Singer at a vintage microphone" style="background:linear-gradient(90deg,#1e3a30,#4a6a60 60%,#d8d8d8)"></div>
    <h3>CATEGORY NAME</h3>
    <p>Nam lacinia tellus ut ipsum blandit ut fringilla augue bibendum. Sed interd-um turpis eget libero ullamcorper vel</p>
  </article>
  <article class="category">
    <div class="category-photo" role="img" aria-label="Cruise ship at sunset" style="background:linear-gradient(180deg,#6a6f80,#c99a60 45%,#3a3d48)"></div>
    <h3>CATEGORY NAME</h3>
    <p>Nam lacinia tellus ut ipsum blandit ut fringilla augue bibendum. Sed interd-um turpis eget libero ullamcorper vel</p>
  </article>
  <article class="category">
    <div class="category-photo" role="img" aria-label="Couple performing with a mandolin" style="background:linear-gradient(90deg,#f2f2f2,#8a7a6a 40%,#eeeeee)"></div>
    <h3>CATEGORY NAME</h3>
    <p>Nam lacinia tellus ut ipsum blandit ut fringilla augue bibendum. Sed interd-um turpis eget libero ullamcorper vel</p>
  </article>
  <article class="category">
    <div class="category-photo" role="img" aria-label="Dancers in colourful costumes" style="background:linear-gradient(180deg,#2a8a7a,#9fb0a8 45%,#e6e6e6)"></div>
    <h3>CATEGORY NAME</h3>
    <p>Nam lacinia tellus ut ipsum blandit ut fringilla augue bibendum. Sed interd-um turpis eget libero ullamcorper vel</p>
  </article>
</div>
<div class="dots" style="top:741px"></div>

<section class="feature">
  <div class="feature-photo"><div role="img" aria-label="Cruise ship lit up at night"></div></div>
  <h2>LOREM IPSUM DOLOR SIT AMET, CONSECTETUR ADIPISCING ELIT</h2>
  <p>Nam lacinia tellus ut ipsum blandit ut fringilla augue bibendum. Sed interdum turpis eget libero ullamcorper vel lobortis purus bibendum. Aliquam erat volutpat. Aenean <a href="#">feugiat nisi a nibh</a> hendrerit blandit. Quisque pharetra lacinia dui nec iaculis. Nullam condimentum justo quis ligula adipiscing non vehicula ligula fermen-tum. Quisque sit amet sapien quam, eget blandit neque. Suspendisse justo massa, facilisis nec adipiscing in, Nam lacinia tellus ut ipsum blandit ut fringilla augue bibendum. Sed interdum turpis eget libero ullamcorper vel lobortis <a href="#">purus bibendum</a>. Aliquam erat volutpat. Aenean feugiat nisi a nibh hendrerit blandit. Quisque pharetra lacinia dui nec iaculis. Nullam condimentum justo quis ligula adipiscing non vehic-ula ligula fermentum. Quisque sit amet sapien quam, eget blandit neque. <a class="read-more" href="#">read more <svg width="6" height="8" viewBox="0 0 6 8"><path d="M0 0l6 4-6 4z" fill="#a9cc3c"/></svg></a></p>
</section>

<footer class="site-footer">
  <p class="copyright">Copyright © 2012 <a href="#">Company Name</a> All rights reserved</p>
  <nav class="footer-nav"><a class="current" href="#">Home</a><a href="#">About</a><a href="#">Blog</a><a href="#">Contact</a></nav>
</footer>

</body>
</html>
```